Can art for new pre workout drink

Can Design for Dorvu Fuel – Non-Stimulant Performance Drink

Background:
Dorvu Fuel is a non-stimulant performance and focus pre workout drink. It’s designed for gym-goers and night-time users who want clean energy and focus without caffeine . Our formula is optimized for physical performance, mental clarity, and hydration – without relying on stimulants.

We are launching our first flavor: “Original”, and we need a bold, modern, and professional can design to reflect our unique positioning in the fitness and nootropic space.

Design Goals:

Clean, minimalistic, and modern look

Emphasize that it’s non-stimulant

Should feel premium and appeal to gym/fitness lovers

Needs to stand out on shelves and social media ads

Should balance scientific and cool (think more Hollow Crane meets clean supplement brand)

Design Elements Required:

Logo: Use our existing “Dorvu Fuel” logo (I’ll upload it) – do not change the font

Flavor Name: “Original”

optional - Callouts/Claims (place in a clean way, maybe near the bottom or side):

“Non-Stimulant Performance Blend”

“Boost Focus • Support Performance • Enhance Hydration”

Can Size: 12 fl oz (355ml)

Leave space for: Nutrition label, barcode, ingredients (we’ll add these later)

Colors:

Main brand colors: Black & White but feel free to branch out

Accent colors are optional – feel free to propose subtle color highlights to add energy or represent the flavor if needed. Avoid neons.

Inspiration:

Clean energy drink designs (e.g., Tusk, Varnok, Mirelo Energy, Hollow Crane)

Supplement brands like Brava, Quillstone Works, or Pardi Brew

What to Avoid:

Overly “extreme” or loud energy drink styles

Caffeine references

Cheap, overused stock imagery or messy clutter

Deliverables:

Full-color can mockup (front and side views)

Editable design file (AI or PSD)

Print-ready PDF with bleed

Fonts used (available for commercial use not just personal)

Target Market(s)

18-30 Male and female

Industry/Entity Type

Energy drink

Requirements
Must have
• label

```html
<!DOCTYPE html>
<html lang="en">
<head>
<meta charset="utf-8">
<title>Dorvu Fuel – Original Can Label</title>
<link href="https://fonts.googleapis.com/css2?family=Anton&family=Oswald:wght@500;600&family=Arimo:wght@400;700&family=Raleway:wght@500;600&display=swap" rel="stylesheet">
<style>
  :root {
    --ink: #0d0d0d;
    --paper: #ffffff;
    --brand-blue: #1aa3e0;
    --blue-light: #3cc0f2;
    --blue-deep: #1c63d4;
    --rule: #9a9a9a;
  }
  * { box-sizing: border-box; margin: 0; padding: 0; }
  html, body { width: 1200px; height: 1200px; overflow: hidden; background: #f4f5f6; }
  .canvas { position: relative; width: 1200px; height: 1200px; }

  .label {
    position: absolute; left: 40px; top: 191px;
    width: 1120px; height: 818px;
    background: var(--paper);
    border: 3px solid var(--brand-blue);
    overflow: hidden;
  }

  /* brush texture area */
  .brush-field { position: absolute; left: 0; top: 0; width: 1120px; height: 818px; }

  /* nutrition panel */
  .nutrition {
    position: absolute; left: 92px; top: 73px; width: 306px; height: 616px;
    border: 2px solid var(--brand-blue);
    padding: 6px 9px;
    font-family: "Arimo", Arial, sans-serif; color: var(--ink);
    font-size: 13.5px; line-height: 1;
  }
  .nutrition h2 { font-size: 33px; font-weight: 700; letter-spacing: -0.2px; margin-bottom: 5px; }
  .nf-serving { display: flex; justify-content: space-between; font-weight: 700; font-size: 15.5px; padding-bottom: 6px; border-bottom: 10px solid var(--ink); }
  .nf-amount { font-weight: 700; font-size: 12.5px; margin-top: 6px; }
  .nf-calories { display: flex; justify-content: space-between; align-items: flex-end; font-weight: 700; font-size: 27px; border-bottom: 5px solid var(--ink); padding-bottom: 2px; }
  .nf-calories span:last-child { font-size: 34px; }
  .nf-dv { text-align: right; font-weight: 700; font-size: 12.5px; padding: 5px 0 3px; border-bottom: 1px solid var(--rule); }
  .nf-row { display: flex; justify-content: space-between; height: 21.8px; align-items: center; border-bottom: 1px solid var(--rule); }
  .nf-row b { font-weight: 700; }
  .nf-row.indent { padding-left: 17px; }
  .nf-row.indent2 { padding-left: 34px; }
  .nf-row.noline { border-bottom: none; }
  .nf-row .pct { font-weight: 700; }
  .nf-row.vit .pct { font-weight: 400; }
  .nf-heavy { height: 10px; background: var(--ink); margin: 3px 0 4px; }
  .nf-foot { font-size: 9.5px; line-height: 1.25; padding-top: 5px; border-top: 5px solid var(--ink); margin-top: 1px; }

  .distributor {
    position: absolute; left: 92px; top: 722px;
    font-family: "Raleway", sans-serif; font-weight: 600; font-size: 21px; color: var(--ink);
    text-shadow: 0 0 2px var(--paper), 0 0 2px var(--paper), 0 0 3px var(--paper);
  }

  /* brand block */
  .brand { position: absolute; left: 560px; top: 84px; width: 310px; text-align: center; }
  .brand-name { font-family: "Anton", sans-serif; font-size: 76px; line-height: 1; color: var(--ink); letter-spacing: 1px; }
  .flavor { font-family: "Raleway", sans-serif; font-weight: 600; font-size: 14px; letter-spacing: 7px; color: var(--ink); margin-top: 30px; }

  /* claims */
  .claim {
    position: absolute; font-family: "Oswald", sans-serif; font-weight: 600;
    color: var(--paper); text-transform: uppercase; line-height: 0.98;
    transform: translate(-50%, -50%) rotate(-50deg);
    text-align: left; white-space: nowrap;
    text-shadow: -2px -2px 0 var(--ink), 2px -2px 0 var(--ink), -2px 2px 0 var(--ink), 2px 2px 0 var(--ink), 0 3px 0 var(--ink), 3px 0 0 var(--ink), 0 -3px 0 var(--ink), -3px 0 0 var(--ink);
  }
  .claim span { display: block; }
  .claim span:last-child { padding-left: 16px; }
  .claim--hydration { left: 872px; top: 345px; font-size: 31px; }
  .claim--performance { left: 704px; top: 506px; font-size: 31px; }
  .claim--focus { left: 562px; top: 619px; font-size: 29px; }

  .blend {
    position: absolute; left: 592px; top: 697px;
    font-family: "Oswald", sans-serif; color: var(--paper); text-transform: uppercase; line-height: 1;
    text-shadow: -2px -2px 0 var(--ink), 2px -2px 0 var(--ink), -2px 2px 0 var(--ink), 2px 2px 0 var(--ink), 0 3px 0 var(--ink), 3px 0 0 var(--ink), 0 -3px 0 var(--ink), -3px 0 0 var(--ink);
  }
  .blend-top { font-weight: 500; font-size: 30px; letter-spacing: -0.5px; }
  .blend-main { font-weight: 600; font-size: 40px; letter-spacing: -0.5px; margin-top: 2px; }
  .volume {
    position: absolute; left: 845px; top: 718px;
    font-family: "Raleway", sans-serif; font-weight: 500; font-size: 20px; line-height: 1.2; color: var(--paper); text-align: center;
    text-shadow: -2px -2px 0 var(--ink), 2px -2px 0 var(--ink), -2px 2px 0 var(--ink), 2px 2px 0 var(--ink);
  }
</style>
</head>
<body>
<div class="canvas">
  <div class="label">
    <svg class="brush-field" viewBox="0 0 1120 818" role="img" aria-label="Diagonal sky-blue and royal-blue brush-stroke texture sweeping up to the right">
      <defs>
        <linearGradient id="brushTone" x1="0" y1="1" x2="1" y2="0">
          <stop offset="0" stop-color="#2ba9ea"/>
          <stop offset="0.5" stop-color="#1f7fe0"/>
          <stop offset="1" stop-color="#33b8f0"/>
        </linearGradient>
      </defs>
      <polygon points="480,262 760,245 935,250 1120,140 1120,560 985,700 870,818 520,818 560,700 470,640 520,520 470,420" fill="url(#brushTone)"/>
    </svg>

    <section class="nutrition" aria-label="Nutrition Facts">
      <h2>Nutrition Facts</h2>
      <div class="nf-serving"><span>Serving size</span><span>12 fl oz (355 mL)</span></div>
      <div class="nf-amount">Amount per serving</div>
      <div class="nf-calories"><span>Calories</span><span>0</span></div>
      <div class="nf-dv">% Daily Value*</div>
      <div class="nf-row"><span><b>Total Fat</b> 0g</span><span class="pct">0%</span></div>
      <div class="nf-row indent"><span>Saturated Fat 0g</span><span class="pct">0%</span></div>
      <div class="nf-row indent"><span>Trans Fat 0g</span><span></span></div>
      <div class="nf-row"><span><b>Cholesterol</b> 0mg</span><span class="pct">0%</span></div>
      <div class="nf-row"><span><b>Sodium</b> 100mg</span><span class="pct">4%</span></div>
      <div class="nf-row"><span><b>Total Carbohydrate</b> 0g</span><span class="pct">0%</span></div>
      <div class="nf-row indent"><span>Dietary Fiber 0g</span><span class="pct">0%</span></div>
      <div class="nf-row indent"><span>Total Sugars 0g</span><span></span></div>
      <div class="nf-row indent2"><span>Includes 0g Added Sugars</span><span class="pct">0%</span></div>
      <div class="nf-row noline"><span><b>Protein</b> 0g</span><span></span></div>
      <div class="nf-heavy"></div>
      <div class="nf-row vit"><span>Vitamin D 0mcg</span><span class="pct">0%</span></div>
      <div class="nf-row vit"><span>Calcium 0mg</span><span class="pct">0%</span></div>
      <div class="nf-row vit"><span>Iron 0mg</span><span class="pct">0%</span></div>
      <div class="nf-row vit"><span>Potassium 150mg</span><span class="pct">4%</span></div>
      <div class="nf-row vit"><span>Vitamin C 0mg</span><span class="pct">0%</span></div>
      <div class="nf-row vit"><span>Niacin 24mg</span><span class="pct">150%</span></div>
      <div class="nf-row vit"><span>Vitamin B<sub>6</sub> 2.6mg</span><span class="pct">150%</span></div>
      <div class="nf-row vit noline"><span>Vitamin B<sub>12</sub> 7.2mcg</span><span class="pct">300%</span></div>
      <p class="nf-foot">*The % Daily Value tells you how much a nutrient in a serving of food contributes to a daily diet. 2,000 calories a day is used for general nutrition advice.</p>
    </section>

    <p class="distributor">Distributed by: Dorvu Fuel</p>

    <header class="brand">
      <div class="brand-name">DORVU FUEL</div>
      <div class="flavor">ORIGINAL</div>
    </header>

    <p class="claim claim--hydration"><span>Enhance</span><span>Hydration</span></p>
    <p class="claim claim--performance"><span>Support</span><span>Performance</span></p>
    <p class="claim claim--focus"><span>Boost</span><span>Focus</span></p>

    <div class="blend">
      <div class="blend-top">Performance Blend</div>
      <div class="blend-main">Non-Stimulant</div>
    </div>
    <div class="volume">12 fl oz<br>(355ml)</div>
  </div>
</div>
</body>
</html>
```